Pemberton Dialworks Business Card Design

Double Sided Business Card Design for a Locksmith company specializing in Safecracking, safe & vault service.

```html
<!DOCTYPE html>
<html lang="en">
<head>
<meta charset="utf-8">
<title>Pemberton Dialworks Business Card</title>
<link rel="stylesheet" href="https://fonts.googleapis.com/css2?family=Krona+One&family=Poppins:wght@400;500&display=swap">
<style>
  :root {
    --stage: #2a2a2a;
    --ink: #0a0a0a;
    --paper: #ffffff;
    --green: #258040;
    --mist: #ececec;
    --text: #111111;
  }
  * { box-sizing: border-box; margin: 0; padding: 0; }
  html, body { width: 1200px; height: 900px; overflow: hidden; background: var(--stage); }
  .stage { position: relative; width: 1200px; height: 900px; }
  .card {
    position: absolute; left: 250px; width: 700px; height: 400px;
    border-radius: 22px; overflow: hidden;
  }
  .card--back { top: 40px; background: var(--ink); }
  .card--front { top: 470px; background: var(--paper); }

  /* Back side */
  .back-circle {
    position: absolute; right: -120px; top: -120px;
    width: 360px; height: 360px; border-radius: 50%; background: var(--green);
  }
  .services {
    position: absolute; left: 50px; top: 175px; z-index: 1;
    font-family: "Krona One", sans-serif; color: var(--paper);
  }
  .services__title { color: var(--green); font-size: 22px; margin-bottom: 12px; letter-spacing: 1px; }
  .services__list { list-style: none; }
  .services__item { font-size: 14px; line-height: 31px; position: relative; padding-left: 24px; letter-spacing: 0.5px; white-space: nowrap; }
  .services__item::before {
    content: ""; position: absolute; left: 0; top: 11px;
    width: 10px; height: 10px; border-radius: 50%; background: var(--green);
  }

  /* Front side */
  .front-circle {
    position: absolute; right: -60px; top: -40px;
    width: 320px; height: 320px; border-radius: 50%; background: var(--mist);
  }
  .brand {
    position: absolute; left: 50px; top: 130px; display: flex; align-items: center; gap: 16px;
  }
  .brand__dot { width: 70px; height: 70px; border-radius: 50%; background: var(--green); flex: none; }
  .brand__name {
    font-family: "Krona One", sans-serif; color: var(--green);
    font-size: 21px; line-height: 30px; width: 230px;
  }
  .divider { position: absolute; left: 365px; top: 60px; width: 1.5px; height: 200px; background: var(--text); }
  .contact { position: absolute; left: 395px; top: 62px; z-index: 1; }
  .contact__name { font-family: "Krona One", sans-serif; color: var(--green); font-size: 22px; }
  .contact__role { font-family: "Krona One", sans-serif; color: var(--text); font-size: 11px; margin: 2px 0 12px; }
  .contact__row {
    display: flex; align-items: flex-start; gap: 12px;
    font-family: "Poppins", sans-serif; font-size: 14px; color: var(--text); line-height: 22px; margin-bottom: 5px;
  }
  .contact__row svg { width: 16px; height: 16px; margin-top: 3px; flex: none; fill: var(--green); }
  .sectors {
    position: absolute; left: 0; bottom: 0; width: 100%; height: 70px; background: var(--ink);
    display: flex; justify-content: center; align-items: center; gap: 42px;
  }
  .sector {
    display: flex; align-items: center; gap: 10px;
    font-family: "Krona One", sans-serif; color: var(--paper); font-size: 16px; letter-spacing: 1px;
  }
  .sector svg { width: 24px; height: 24px; fill: var(--green); }
</style>
</head>
<body>
<main class="stage">
  <section class="card card--back">
    <div class="back-circle"></div>
    <div class="services">
      <h2 class="services__title">OUR SERVICES</h2>
      <ul class="services__list">
        <li class="services__item">24-HOUR EMERGENCY LOCKSMITH</li>
        <li class="services__item">KEY CUTTING &amp; SAFES</li>
        <li class="services__item">ALARMS &amp; CAMERAS</li>
        <li class="services__item">MULTI-POINT STRIP LOCKS</li>
      </ul>
    </div>
  </section>

  <section class="card card--front">
    <div class="front-circle"></div>
    <div class="brand">
      <div class="brand__dot"></div>
      <div class="brand__name">PEMBERTON DIALWORKS</div>
    </div>
    <div class="divider"></div>
    <div class="contact">
      <div class="contact__name">OWEN HARTLEY</div>
      <div class="contact__role">LOCKSMITH</div>
      <div class="contact__row">
        <svg viewBox="0 0 24 24"><path d="M6.6 10.8a15 15 0 0 0 6.6 6.6l2.2-2.2a1 1 0 0 1 1-.25 11.4 11.4 0 0 0 3.6.57 1 1 0 0 1 1 1V20a1 1 0 0 1-1 1A17 17 0 0 1 3 4a1 1 0 0 1 1-1h3.5a1 1 0 0 1 1 1c0 1.25.2 2.45.57 3.57a1 1 0 0 1-.25 1z"/></svg>
        <span>555-0142-7788</span>
      </div>
      <div class="contact__row">
        <svg viewBox="0 0 24 24"><path d="M2 5h20v14H2z M2 5l10 8 10-8" /></svg>
        <span>info@pembertondialworks.com</span>
      </div>
      <div class="contact__row">
        <svg viewBox="0 0 24 24"><path d="M12 2a10 10 0 1 0 0 20 10 10 0 0 0 0-20zm0 2c.9 1.2 1.6 2.8 1.9 5h-3.8c.3-2.2 1-3.8 1.9-5zM4.3 11h3.7a16 16 0 0 0 .4 4H5a8 8 0 0 1-.7-4zm11.7 0h3.7a8 8 0 0 1-.7 4h-3.4a16 16 0 0 0 .4-4zm-6 0h4a14 14 0 0 1-.4 4h-3.2a14 14 0 0 1-.4-4z"/></svg>
        <span>www.pembertondialworks.com</span>
      </div>
      <div class="contact__row">
        <svg viewBox="0 0 24 24"><path d="M12 2a7 7 0 0 0-7 7c0 5 7 13 7 13s7-8 7-13a7 7 0 0 0-7-7zm0 9.5A2.5 2.5 0 1 1 12 6.5a2.5 2.5 0 0 1 0 5z"/></svg>
        <span>418 Larkspur Lane<br>Suite 12, Fairhaven<br>OR 97401</span>
      </div>
    </div>
    <div class="sectors">
      <div class="sector">
        <svg viewBox="0 0 24 24"><path d="M12 3 2 12h3v9h5v-6h4v6h5v-9h3z"/></svg>RESIDENTIAL
      </div>
      <div class="sector">
        <svg viewBox="0 0 24 24"><path d="M3 21V5h9v16zm10 0V10h8v11zM5 7v2h2V7zm3 0v2h2V7zM5 11v2h2v-2zm3 0v2h2v-2zm7 1v2h2v-2zm3 0v2h2v-2z"/></svg>COMMERCIAL
      </div>
      <div class="sector">
        <svg viewBox="0 0 24 24"><path d="M5 11l2-5h10l2 5h1v6h-2v2h-3v-2H9v2H6v-2H4v-6zm2.5 0h9l-1.2-3H8.7zM7 13a1.3 1.3 0 1 0 0 2.6A1.3 1.3 0 0 0 7 13zm10 0a1.3 1.3 0 1 0 0 2.6 1.3 1.3 0 0 0 0-2.6z"/></svg>AUTOMOTIVE
      </div>
    </div>
  </section>
</main>
</body>
</html>
```